ClipNestra.com - Landing Page

I need a Landing Page to present ClipNestra.com. It is a Platform that will allow people to COLLABORATE to produce Video Projects (Movies, Documentaries, Tv Shows etc).

As I described in the comments AT THE BEGINNING there will be just one Social Movie (is how we call a Video Project) featured in the Landing Page and others will follow.

In the Landing Page I need just the BASIC features of a WebSite to keep contact with who is interested in the Project (email contact etc).
Updates

Project Deadline Extended
Reason: Dears in the last few days several designers showed interest in submitting a Design for this project. I think is better if I give few days more for them to prepare their submissions. So I extended the deadline for 7 days Thanks Tomas

Target Market(s)

Wannabe Video Directors/ Producers around the world

Industry/Entity Type

Movie

Requirements
Must have
• a) Designed to be ready for Responsive Web Design.

b) Landing Page with possible infinite Scrolling

c) At the Centre of the Page there must the Space for to embed an image that is a link to another WebSite that is under construction. This other WebSite is the first Experiment of a Collaborative Video Production over the Web

d) Even if the ClipNestra Logo is in Black and White (see below 2 versions) there is no need that the Site is in Black and White. The colors fit the Logo
Should not have
• a) Parallax

```html
<!DOCTYPE html>
<html lang="en">
<head>
<meta charset="UTF-8">
<title>ClipNestra.com – Landing Page</title>
<link rel="stylesheet" href="https://fonts.googleapis.com/css2?family=Roboto+Condensed:wght@700&family=Kaushan+Script&display=swap">
<style>
  :root {
    --charcoal: #3a3a3a;
    --paper: #ffffff;
    --band: #151515;
    --gold: #c9962e;
    --gold-light: #e8c36a;
    --gold-dark: #9c6f18;
    --play-orange: #f0a83a;
    --text-light: #ffffff;
  }
  * { box-sizing: border-box; margin: 0; padding: 0; }
  html, body { width: 774px; height: 1200px; overflow: hidden; }
  body { position: relative; background: var(--paper); font-family: "Roboto Condensed", sans-serif; }

  .site-header { position: absolute; left: 0; top: 0; width: 774px; height: 190px; background: var(--charcoal); }
  .brand { position: absolute; top: 58px; left: 0; width: 100%; display: flex; justify-content: center; align-items: center; gap: 12px; }
  .brand-square { width: 56px; height: 56px; background: var(--text-light); }
  .brand-name { color: var(--text-light); font-size: 64px; font-weight: 700; letter-spacing: 1px; line-height: 1; }

  .stills-band { position: absolute; left: 13px; width: 748px; height: 96px; background: var(--band);
    border-top: 3px solid var(--gold); border-bottom: 3px solid var(--gold); padding: 18px 8px; }
  .stills-band.top { top: 194px; }
  .stills-band.bottom { top: 730px; }
  .stills-fill { width: 100%; height: 100%;
    background: linear-gradient(90deg, #8a6a50, #9a9a9a 22%, #c8602a 42%, #8a9a50 58%, #d88a30 75%, #c0404a); }
  .stills-band.bottom .stills-fill {
    background: linear-gradient(90deg, #c8602a, #9a9a9a 22%, #c0404a 42%, #d88a30 58%, #8a6a50 78%, #a0a0a0); }

  .feature-video { position: absolute; left: 142px; top: 382px; width: 490px; height: 276px;
    border: 8px solid var(--gold); background: linear-gradient(180deg, #6f8a52 0%, #8fae5e 55%, #a8b894 100%); }
  .feature-title { position: absolute; top: 10px; left: 0; width: 100%; text-align: center;
    font-family: "Kaushan Script", cursive; color: var(--text-light); font-size: 37px; }
  .play-button { position: absolute; left: 50%; top: 56%; transform: translate(-50%, -50%); }

  .site-footer { position: absolute; left: 0; top: 840px; width: 774px; height: 360px; background: var(--charcoal); }
  .signup-title { position: absolute; top: 50px; width: 100%; text-align: center;
    font-family: "Kaushan Script", cursive; color: var(--text-light); font-size: 46px; font-weight: 400; }
  .email-field { position: absolute; left: 206px; top: 122px; width: 362px; height: 40px;
    border: 5px solid var(--gold); background: var(--paper); }
  .submit-button { position: absolute; left: 310px; top: 187px; width: 155px; height: 44px;
    border: 2px solid var(--gold-dark); border-radius: 4px;
    background: linear-gradient(180deg, var(--gold-light), var(--gold) 55%, var(--gold-dark));
    color: var(--text-light); font-family: "Roboto Condensed", sans-serif; font-weight: 700; font-size: 24px; letter-spacing: 1px; }
</style>
</head>
<body>
  <header class="site-header">
    <div class="brand"><span class="brand-square"></span><span class="brand-name">ClipNestra.com</span></div>
  </header>

  <div class="stills-band top">
    <div class="stills-fill" role="img" aria-label="Film strip of movie stills"></div>
  </div>

  <main>
    <a class="feature-video" role="img" aria-label="Video still of people walking in a park with a cyclist">
      <span class="feature-title">Watch more video project!</span>
      <svg class="play-button" width="110" height="110" viewBox="0 0 110 110" aria-hidden="true">
        <circle cx="55" cy="55" r="50" fill="#2b2b2b" fill-opacity="0.85"/>
        <circle cx="55" cy="55" r="40" fill="none" stroke="#4a4a4a" stroke-width="4"/>
        <polygon points="44,34 80,55 44,76" fill="var(--play-orange)"/>
      </svg>
    </a>
  </main>

  <div class="stills-band bottom">
    <div class="stills-fill" role="img" aria-label="Film strip of movie stills"></div>
  </div>

  <footer class="site-footer">
    <h2 class="signup-title">Your Email here!</h2>
    <div class="email-field"></div>
    <button class="submit-button" type="button">SUBMIT</button>
  </footer>
</body>
</html>
```